Fenwick Law PC business card. National Consumer Law Firm with principal office in San Francisco. We maintain additional offices in Meridian, Mississippi and Birmingham, Alabama. We protect consumers against unscrupulous mega corporations. We want to covey integrity and a willingness to take on the Goliaths of the corporate world. I like red accents. Try to use uploaded picture of Harbor Arch Span or a sketch. Licensed in California, Alabama and Mississippi. Main office: 317 Alder Ave. #408, San Francisco, CA 94110, ph. 415/555-0193, 800/555-0147 (fax), 205/555-0162 (AL).
www.fenwicklawpc.example
www.buyerguard.example.
At top--Consumer Class Litigation in red. Also Fenwick Law PC at top in red. Then red horizontal line please. Or if you have another idea. I have not seen new logo.
After line on left at top
L. Thomas Fenwick
Attorney
Cell 205/555-0178
thomas@fenwicklawpc.example
Offices: San Francisco, CA, Birmingham, AL, Charlotte, NC and Meridian, MS

I asked that the very bottom of the BUSINESS CARD TO SAY "Offices in California, North Carolina, Alabama and Mississippi NOT STATES WHERE I AM LICENSED. I.E., I AM NOT LICENSED IN NOTH CAROLINA I NEED NEW FILES IF YOU CAN GET THEM IN THE MORNING MY TIME. WHERE CAN I FIND THE NEW FILES ONCE YOU MODIFY.

for North Carolina, I need an asterick where it is listed. "not licensed will associate counsel" AGAIN NORTH CAROLINA IS 2 WORDS WITH A SPACE BETWEEN THEM

For Biz card, put tollfree number (888)555-0121 and toll free fax (800)555-0147 somewhere like below my cell number or wherever you can. States where I have offices at the bottom: California, North Carolina, Alabama and Mississippi.

For Biz card, put tollfree number (888)555-0121 and toll free fax (800)555-0147 somewhere like below my cell number or wherever you can. States where I have offices at the bottom: California, North Carolina, Alabama and Mississippi. AstericK *North Carolina--not licensed will associate co-counel. Same with letterhead and website. I need to disclose not licensed to practice in North Carolina.

```html
<!DOCTYPE html>
<html lang="en">
<head>
<meta charset="utf-8">
<title>Fenwick Law PC – Business Card</title>
<link rel="stylesheet" href="https://fonts.googleapis.com/css2?family=Roboto+Condensed:wght@300;400;700&family=Open+Sans:wght@400;600&display=swap">
<style>
  :root {
    --page-bg: #ecebe8;
    --accent-red: #e4202e;
    --ink-dark: #262626;
    --text-white: #ffffff;
    --sky-light: #e6e6e6;
    --fog-mid: #b9b9b9;
    --water-dark: #5d5d5d;
    --shore-deep: #3a3a3a;
  }
  * { box-sizing: border-box; margin: 0; padding: 0; }
  html, body {
    width: 1200px;
    height: 800px;
    overflow: hidden;
    background: var(--page-bg);
  }
  .business-card {
    position: absolute;
    left: 75px;
    top: 100px;
    width: 1050px;
    height: 600px;
    overflow: hidden;
    box-shadow: 0 6px 24px rgba(0, 0, 0, 0.18);
  }
  .harbor-artwork {
    position: absolute;
    inset: 0;
    background:
      linear-gradient(100deg, rgba(40,40,40,0.55) 0%, rgba(40,40,40,0) 28%),
      linear-gradient(180deg, var(--sky-light) 0%, var(--sky-light) 32%, var(--fog-mid) 50%, var(--water-dark) 72%, var(--shore-deep) 100%);
  }
  .firm-mark {
    position: absolute;
    left: 260px;
    top: 36px;
  }
  .firm-name {
    font-family: "Roboto Condensed", sans-serif;
    font-weight: 700;
    font-size: 46px;
    color: var(--ink-dark);
    letter-spacing: 0.5px;
    line-height: 1;
  }
  .firm-tagline {
    margin-top: 10px;
    font-family: "Roboto Condensed", sans-serif;
    font-weight: 400;
    font-size: 24px;
    color: var(--accent-red);
  }
  .attorney-block {
    position: absolute;
    right: 36px;
    top: 132px;
    text-align: right;
  }
  .attorney-name {
    display: inline-block;
    background: var(--accent-red);
    color: var(--text-white);
    font-family: "Roboto Condensed", sans-serif;
    font-weight: 300;
    font-size: 58px;
    line-height: 1;
    padding: 12px 18px 10px;
    text-transform: uppercase;
    letter-spacing: -0.5px;
  }
  .attorney-title {
    display: inline-block;
    background: var(--accent-red);
    color: var(--text-white);
    font-family: "Open Sans", sans-serif;
    font-size: 22px;
    padding: 4px 18px 6px 60px;
    border-top: 2px dashed var(--text-white);
  }
  .contact-list {
    position: absolute;
    right: 36px;
    bottom: 84px;
    list-style: none;
    text-align: right;
  }
  .contact-item {
    display: block;
  }
  .contact-item span {
    display: inline-block;
    background: var(--accent-red);
    color: var(--text-white);
    font-family: "Open Sans", sans-serif;
    font-size: 26px;
    line-height: 1.2;
    padding: 1px 16px 3px;
    border-bottom: 2px dashed var(--text-white);
  }
  .contact-label {
    font-size: 18px;
    opacity: 0.9;
    margin-right: 6px;
  }
  .office-footer {
    position: absolute;
    left: 36px;
    right: 36px;
    bottom: 14px;
    text-align: right;
    font-family: "Open Sans", sans-serif;
    color: var(--text-white);
  }
  .office-states {
    font-size: 18px;
    font-weight: 600;
    line-height: 1.4;
  }
  .office-disclaimer {
    font-size: 14px;
    line-height: 1.4;
    opacity: 0.9;
  }
</style>
</head>
<body>
  <main class="business-card">
    <div class="harbor-artwork" role="img" aria-label="Grayscale sketch of the Harbor Arch Span over the bay with the city shoreline"></div>

    <header class="firm-mark">
      <p class="firm-name">Fenwick Law PC</p>
      <p class="firm-tagline">Consumer Class Litigation</p>
    </header>

    <section class="attorney-block">
      <h1 class="attorney-name">L. Thomas Fenwick</h1><br>
      <p class="attorney-title">Attorney</p>
    </section>

    <ul class="contact-list">
      <li class="contact-item"><span><small class="contact-label">Cell</small>205/555-0178</span></li>
      <li class="contact-item"><span><small class="contact-label">Toll-free</small>(888)555-0121</span></li>
      <li class="contact-item"><span><small class="contact-label">Toll-free fax</small>(800)555-0147</span></li>
      <li class="contact-item"><span>thomas@fenwicklawpc.example</span></li>
      <li class="contact-item"><span>www.fenwicklawpc.example</span></li>
    </ul>

    <footer class="office-footer">
      <p class="office-states">Offices in California, North Carolina*, Alabama and Mississippi</p>
      <p class="office-disclaimer">*North Carolina: not licensed, will associate co-counsel</p>
    </footer>
  </main>
</body>
</html>
```